Family owned plumbing contractor needs eye catching business card design

Business cards that are unique, eye catching, and provide customers with general company information, such as name, address, phone number, website, employee name/title, cell phone #, & email address. We are transitioning to a new logo that utilizes a more retro feel, so we are interested in seeing some cool old school designs in the mix. We are liking the dark background on some of the samples on this website. If that is workable with our artwork, we would like to see that incorporated into the design.
Contact Information for Business Card
Copperline Pipeworks, Inc.
www.copperlinepipeworks.example
(555) 392-7068 phone
Nevada License #64205
California License #5810473
Dale Wrennick, President
(555) 618-9032 cell
dale@copperlinepipeworks.example
Residential * Commercial * Service
Requirements
Must have
- The business card details listed above & logo provided.
Nice to have
- I made some notes about color options in the description.

```html
<!DOCTYPE html>
<html lang="en">
<head>
<meta charset="utf-8">
<title>Copperline Pipeworks, Inc. — Business Card</title>
<link rel="stylesheet" href="https://fonts.googleapis.com/css2?family=Berkshire+Swash&family=Jost:wght@400;500&display=swap">
<style>
  :root {
    --page-bg: #ece8e2;
    --card-blue: #4f7391;
    --card-blue-light: #5b809d;
    --mint: #72c7a6;
    --text-light: #f1f4f6;
    --card-paper: #f3f2ee;
    --paper-shade: #e4e7e9;
    --ink-blue: #44627d;
    --shadow: rgba(60, 50, 40, 0.18);
  }
  * { margin: 0; padding: 0; box-sizing: border-box; }
  html, body {
    width: 1200px;
    height: 800px;
    overflow: hidden;
    background: var(--page-bg);
  }
  .sheet {
    width: 1200px;
    height: 800px;
    display: flex;
    flex-direction: column;
    align-items: center;
    justify-content: center;
    gap: 40px;
  }
  .card {
    position: relative;
    width: 560px;
    height: 320px;
    box-shadow: 0 3px 10px var(--shadow);
    overflow: hidden;
  }
  .card-texture {
    position: absolute;
    inset: 0;
  }
  .card--front { background: var(--card-blue); }
  .card--front .card-texture {
    background: radial-gradient(ellipse at 45% 35%, var(--card-blue-light) 0%, var(--card-blue) 70%);
  }
  .card--back { background: var(--card-paper); }
  .card--back .card-texture {
    background: radial-gradient(ellipse at 50% 50%, var(--card-paper) 40%, var(--paper-shade) 100%);
  }
  .contact-block {
    position: absolute;
    left: 0;
    right: 0;
    top: 96px;
    text-align: center;
    font-family: 'Jost', sans-serif;
    color: var(--text-light);
  }
  .person-name {
    font-family: 'Berkshire Swash', cursive;
    font-size: 29px;
    line-height: 1;
    color: var(--mint);
  }
  .person-title {
    font-family: 'Berkshire Swash', cursive;
    font-size: 17px;
    line-height: 1;
    margin-top: 3px;
    color: var(--mint);
  }
  .company-line {
    font-size: 13px;
    margin-top: 14px;
  }
  .phone-line {
    font-size: 14px;
    margin-top: 10px;
  }
  .web-line,
  .license-line {
    font-size: 13px;
    margin-top: 4px;
  }
  .license-line { margin-top: 6px; }
  .brand-mark {
    position: absolute;
    left: 0;
    right: 0;
    top: 130px;
    display: flex;
    align-items: center;
    justify-content: center;
    gap: 12px;
  }
  .brand-dot {
    width: 18px;
    height: 18px;
    border-radius: 50%;
    background: var(--ink-blue);
  }
  .brand-name {
    font-family: 'Jost', sans-serif;
    font-weight: 500;
    font-size: 30px;
    color: var(--ink-blue);
  }
  .service-line {
    position: absolute;
    left: 0;
    right: 0;
    top: 274px;
    text-align: center;
    font-family: 'Jost', sans-serif;
    font-size: 13px;
    letter-spacing: 0.3px;
    color: var(--ink-blue);
  }
</style>
</head>
<body>
  <main class="sheet">
    <section class="card card--front">
      <div class="card-texture" role="img" aria-label="Faint tonal flame pattern across the blue card background"></div>
      <div class="contact-block">
        <p class="person-name">Dale Wrennick</p>
        <p class="person-title">President</p>
        <p class="company-line">Copperline Pipeworks, Inc.</p>
        <p class="phone-line">Tel. (555) 392-7068 Mob. (555) 618-9032</p>
        <p class="web-line">dale@copperlinepipeworks.example www.copperlinepipeworks.example</p>
        <p class="license-line">California License #5810473 Nevada License #64205</p>
      </div>
    </section>

    <section class="card card--back">
      <div class="card-texture" role="img" aria-label="Light distressed crackle texture on off-white paper"></div>
      <div class="brand-mark">
        <span class="brand-dot"></span>
        <span class="brand-name">Copperline Pipeworks, Inc.</span>
      </div>
      <p class="service-line">RESIDENTIAL · COMMERCIAL · SERVICE</p>
    </section>
  </main>
</body>
</html>
```